Business Card Design for Varnok Facility Services

We are looking for a Business Card Design for the Company "Varnok Facility Services."
Front side:
- Company Logo (small)
- Company Name, address, pohone, website and personal data.
- white background, for text e.g. company colors (blue or green like in the logo)
Please use following data:
Company data:
Varnok Facility Services Tulbrecht
Kirchmattweg 12
6331 Cham
www.varnok-fs.ch
Person data:
Ruben Tulbrecht
Geschäftsführer
+41 76 519 84 60
info@varnok-fs.ch
Back side:
could be colored in blue or green
please use a big logo sing and some smaller icons to say what is all beeing offered in facility services, like cleaning, maintenance cleaning
industrial cleaning, caretaking, gardening, disposal. There is no need for everyone of the icons if there are similar or an icon is standing for more of them.
Cleaning Service
colors to use:
blue: HEX 246BB0
green: HEX 52B33E

```html
<!DOCTYPE html>
<html lang="de">
<head>
<meta charset="utf-8">
<title>Varnok Facility Services – Business Card</title>
<link rel="stylesheet" href="https://fonts.googleapis.com/css2?family=Montserrat:wght@600;700&family=Roboto:wght@400;500;700&display=swap">
<style>
  :root {
    --blue: #246BB0;
    --green: #52B33E;
    --green-light: #7cc242;
    --white: #ffffff;
    --stage: #ece9e4;
  }
  * { margin: 0; padding: 0; box-sizing: border-box; }
  html, body { width: 900px; height: 1200px; overflow: hidden; }
  body { background: var(--stage); font-family: "Roboto", Arial, sans-serif; position: relative; }

  .card {
    position: absolute; left: 80px; width: 735px; height: 428px;
    border-radius: 22px; overflow: hidden;
    box-shadow: 0 6px 16px rgba(0,0,0,.25);
  }
  .card-front { top: 128px; background: var(--white); }
  .card-back { top: 646px; height: 430px; }

  .front-waves { position: absolute; inset: 0; width: 100%; height: 100%; }

  .sparkle-area {
    position: absolute; left: 590px; top: 6px; width: 140px; height: 120px;
    border-radius: 30px;
    background: radial-gradient(circle, rgba(82,179,62,.14), rgba(36,107,176,0) 70%);
  }

  .brand-front {
    position: absolute; left: 52px; top: 66px;
    display: flex; align-items: center; gap: 14px;
  }
  .brand-dot { width: 44px; height: 44px; border-radius: 50%; background: var(--green); }
  .brand-front .brand-name {
    font-family: "Roboto", Arial, sans-serif; font-weight: 500;
    font-size: 34px; color: var(--blue); letter-spacing: 1px; line-height: 1;
  }

  .company-block { position: absolute; left: 52px; top: 186px; color: var(--blue); }
  .company-name { font-size: 17.5px; font-weight: 500; margin-bottom: 6px; }
  .company-name .accent { color: var(--green); }
  .address-line { font-size: 16px; line-height: 22px; }
  .web-dash { width: 6px; height: 2px; background: var(--green); margin: 10px 0 6px; }
  .website { font-size: 17px; font-weight: 700; color: var(--green); }

  .person-block {
    position: absolute; right: 52px; top: 292px; text-align: right; color: var(--white);
  }
  .person-name {
    font-family: "Montserrat", Arial, sans-serif; font-weight: 600;
    font-size: 18px; letter-spacing: 1.6px; text-transform: uppercase;
  }
  .person-role {
    font-family: "Montserrat", Arial, sans-serif; font-weight: 700;
    font-size: 13.5px; letter-spacing: .8px; margin-top: 8px; text-transform: uppercase;
  }
  .contact-list { list-style: none; margin-top: 12px; }
  .contact-item {
    display: flex; justify-content: flex-end; align-items: center; gap: 8px;
    font-size: 16px; line-height: 26px;
  }
  .contact-icon {
    width: 19px; height: 19px; border-radius: 50%; background: var(--green);
    display: flex; align-items: center; justify-content: center;
  }

  .back-pattern {
    position: absolute; inset: 0;
    background: linear-gradient(60deg, var(--blue) 0%, #1f9a8a 45%, #2bb24a 72%, var(--green-light) 100%);
  }
  .brand-back {
    position: absolute; left: 0; right: 0; top: 200px; text-align: center;
    display: flex; flex-direction: column; align-items: center; gap: 18px;
  }
  .brand-back .brand-dot { width: 90px; height: 90px; background: var(--white); opacity: .95; }
  .brand-back .brand-name {
    position: absolute; top: 110px; left: 0; right: 0;
    font-family: "Roboto", Arial, sans-serif; font-weight: 500;
    font-size: 38px; letter-spacing: 2px; color: var(--white);
  }
  .brand-back { top: 110px; }

  .service-list {
    position: absolute; left: 0; right: 0; top: 342px; text-align: center;
    color: var(--white); font-size: 17.5px; font-weight: 500; line-height: 28px;
  }
  .service-sep {
    display: inline-block; width: 8px; height: 8px; border-radius: 50%;
    background: var(--green-light); border: 1px solid var(--white);
    margin: 0 4px; vertical-align: middle;
  }
</style>
</head>
<body>

<section class="card card-front" aria-label="Business card front">
  <svg class="front-waves" viewBox="0 0 735 428" aria-hidden="true">
    <path d="M0,362 C180,392 330,370 470,290 C570,232 650,205 735,205 V428 H0 Z" fill="var(--blue)"/>
    <path d="M0,348 C190,372 330,350 460,275 C560,217 650,188 735,188 V205 C650,205 570,232 470,290 C330,370 180,392 0,362 Z" fill="var(--white)"/>
    <path d="M85,336 C290,360 410,300 510,238 C590,190 670,166 735,165 V186 C655,188 585,214 500,266 C400,326 260,356 85,336 Z" fill="var(--green)"/>
    <path d="M85,340 C250,352 350,318 440,272 C350,330 250,356 85,340 Z" fill="var(--green-light)"/>
  </svg>

  <div class="sparkle-area" role="img" aria-label="Small decorative sparkles"></div>

  <div class="brand-front">
    <span class="brand-dot"></span>
    <span class="brand-name">Varnok Facility Services</span>
  </div>

  <div class="company-block">
    <p class="company-name">Varnok <span class="accent">Facility Services</span> Tulbrecht</p>
    <p class="address-line">Kirchmattweg 12</p>
    <p class="address-line">6331 Cham</p>
    <div class="web-dash"></div>
    <p class="website">www.varnok-fs.ch</p>
  </div>

  <div class="person-block">
    <p class="person-name">Ruben Tulbrecht</p>
    <p class="person-role">Geschäftsführer</p>
    <ul class="contact-list">
      <li class="contact-item">+41 76 519 84 60
        <span class="contact-icon">
          <svg width="11" height="11" viewBox="0 0 24 24"><path fill="#fff" d="M6.6 10.8a15 15 0 0 0 6.6 6.6l2.2-2.2c.3-.3.7-.4 1-.2 1.1.4 2.3.6 3.6.6.6 0 1 .4 1 1V20c0 .6-.4 1-1 1A17 17 0 0 1 3 4c0-.6.4-1 1-1h3.5c.6 0 1 .4 1 1 0 1.3.2 2.5.6 3.6.1.3 0 .7-.2 1z"/></svg>
        </span>
      </li>
      <li class="contact-item">info@varnok-fs.ch
        <span class="contact-icon">
          <svg width="11" height="11" viewBox="0 0 24 24"><path fill="#fff" d="M2 5h20v14H2z"/><path fill="none" stroke="#52B33E" stroke-width="2" d="M2 6l10 7 10-7"/></svg>
        </span>
      </li>
    </ul>
  </div>
</section>

<section class="card card-back" aria-label="Business card back">
  <div class="back-pattern" role="img" aria-label="Faint pattern of facility service icons over a blue to green gradient"></div>

  <div class="brand-back">
    <span class="brand-dot"></span>
    <span class="brand-name">Varnok Facility Services</span>
  </div>

  <div class="service-list">
    <p>Cleaning <span class="service-sep"></span> Maintenance cleaning <span class="service-sep"></span> Industrial cleaning</p>
    <p>Caretaking <span class="service-sep"></span> Gardening <span class="service-sep"></span> Disposal.</p>
  </div>
</section>

</body>
</html>
```